Business Card Needed for Crafter of Pottery, Jewelry and Artwork

Calling all designers in search of an artistic challenge.

I need a new business card design for my pottery, jewelry and artwork business, Woven Glass and Tide, based in Vancouver BC.

I would like a card that is bright and inviting and preferably incorporates my logo and a sample of photos of my work while having a clean fresh look. The following contact details would preferably be included on the card as well:
• Melinda Osgood
• Designer
• Phone: 604.555.0147
• Email: Designer@WovenGlassandTide.example
• Website: www.WovenGlassandTide.example
• Blog: www.KilnNotesDaily.example

The logo is attached in two color schemes in both Vector and Source formats. On past cards I’ve also included photos of my work. By including photos of the work the pieces are showcased and it catches people’s eye and prompts them to pick up the card and look at it more closely. For example, if I leave a stack in a coffee shop I want people to be drawn to the card, to pick it up and get a sense of the my product lines. Please feel free to pull photos of my work directly off of my website. If you need photos with higher pixels please let me know and I’ll email them directly to you. The website background is bffbda (191, 251, 218). I would like the business cards to match the feel of the website for consistency but the cards do not need to use the exact same colors. My website and current business card are predominantly turquoise shades. The background uses stripes provided by the website template. I don’t know the exact colors of the stripes.

My current business card is attached to show the use of photos in a design. Please note that I am not thrilled with my own design and am looking for variations and completely new designs. This example is not meant to be used as a template or starting point.

Here is some background surrounding my company:
WGT offers one of a kind jewelry, pottery, artwork and leather bags each designed with a twist. The pottery varies from rustic every day functional ware to raku artwork. The jewelry ranges from simple sterling every day pieces to multimedia pieces incorporating stone, metal, ceramics and fabric. The artwork is multimedia, typically acrylic paired with a natural element such as bark. All the bags are leather with reworked kimono fabric or patterned silk lining.

Feel free to check out my website to get a flavour for my work and the color scheme I've used on marketing materials so far. www.wovenglassandtide.example
Updates

Thank you to everyone who has submitted a design so far. I hope everyone has received some helpful feedback.

I'm going to post a survey to customers and friends asking for their votes. If you have new designs to submit please try to get them in by Saturday March 30 at noon so that I can include it in the survey launch.

Thank you

Target Market(s)

Females aged 25-65 interested in one of a kind functional pottery and jewelry.

Industry/Entity Type

Coffee Shop

Requirements
Must have
• Contact information, website, blog
Nice to have
• Logo, photos

```html
<!DOCTYPE html>
<html lang="en">
<head>
<meta charset="utf-8">
<title>Woven Glass and Tide – Business Cards</title>
<link rel="stylesheet" href="https://fonts.googleapis.com/css2?family=Source+Sans+3:ital,wght@0,300;0,400;0,600;1,300&display=swap">
<style>
  :root {
    --stage: #3a3a3a;
    --teal: #3fa9a3;
    --teal-light: #58b9b3;
    --teal-deep: #1f8a84;
    --teal-band: #2f9a94;
    --teal-band-light: #5fc0ba;
    --navy: #2b2a63;
    --white: #ffffff;
    --ring: #2a8f89;
    --blog-label: #1fb3c4;
    --stripe: rgba(255, 255, 255, 0.07);
    --stripe-dark: rgba(0, 60, 58, 0.06);
    --photo-bag: #9aa3a6;
    --photo-necklace: #8fa69a;
    --photo-bowl: #b9a48a;
    --photo-mugs: #7f9aa3;
  }
  html, body {
    margin: 0;
    width: 1200px;
    height: 949px;
    overflow: hidden;
    background: var(--stage);
    font-family: "Source Sans 3", "Segoe UI", sans-serif;
  }
  .card {
    position: absolute;
    left: 232px;
    width: 735px;
    height: 420px;
    overflow: hidden;
    background:
      repeating-linear-gradient(100deg, var(--stripe) 0 1px, transparent 1px 3px, var(--stripe-dark) 3px 4px, transparent 4px 6px),
      linear-gradient(160deg, var(--teal-light) 0%, var(--teal) 55%, #389f99 100%);
  }
  .card--front { top: 40px; }
  .card--back  { top: 489px; }

  /* Front */
  .brand-name {
    position: absolute;
    top: 26px;
    left: 0;
    width: 100%;
    text-align: center;
    margin: 0;
    font-size: 36px;
    font-weight: 600;
    letter-spacing: 3px;
    color: var(--navy);
  }
  .product-row {
    position: absolute;
    top: 96px;
    left: 26px;
    display: flex;
    gap: 8px;
    z-index: 2;
    margin: 0;
    padding: 0;
    list-style: none;
  }
  .product {
    width: 164px;
    height: 164px;
    border-radius: 50%;
    border: 5px solid var(--ring);
    box-sizing: border-box;
    padding: 4px;
    background: var(--white);
  }
  .product__photo {
    width: 100%;
    height: 100%;
    border-radius: 50%;
  }
  .product__photo--bag { background: radial-gradient(circle at 40% 45%, #b7bdbf, var(--photo-bag)); }
  .product__photo--necklace { background: radial-gradient(circle at 50% 45%, #aebfb4, var(--photo-necklace)); }
  .product__photo--bowl { background: radial-gradient(circle at 50% 50%, #d6c6ae, var(--photo-bowl)); }
  .product__photo--mugs { background: radial-gradient(circle at 50% 50%, #a2b7bd, var(--photo-mugs)); }

  .web-band {
    position: absolute;
    top: 300px;
    left: 0;
    width: 100%;
    height: 46px;
    background: var(--teal-band);
  }
  .web-band__url {
    position: absolute;
    top: 10px;
    left: 270px;
    font-size: 21px;
    color: var(--white);
  }
  .web-band-under {
    position: absolute;
    top: 346px;
    left: 0;
    width: 100%;
    height: 26px;
    background: var(--teal-band-light);
  }

  /* Back */
  .brand-badge {
    position: absolute;
    top: 92px;
    left: 58px;
    width: 196px;
    height: 196px;
    border-radius: 50%;
    background: var(--white);
    box-shadow: 0 0 0 6px var(--teal-deep);
    display: flex;
    align-items: center;
    justify-content: center;
    text-align: center;
  }
  .brand-badge__name {
    margin: 0;
    width: 160px;
    font-size: 26px;
    font-weight: 600;
    line-height: 1.15;
    letter-spacing: 1px;
    color: var(--navy);
  }
  .contact {
    position: absolute;
    top: 132px;
    left: 360px;
    margin: 0;
    font-style: normal;
    color: var(--white);
  }
  .contact__name {
    margin: 0;
    font-size: 29px;
    font-weight: 600;
  }
  .contact__role {
    margin: 0;
    font-size: 27px;
    font-weight: 300;
    font-style: italic;
    color: var(--teal-deep);
  }
  .contact__phone {
    margin: 0;
    font-size: 27px;
    font-weight: 400;
  }
  .contact__email {
    margin: 6px 0 0;
    font-size: 17px;
    font-weight: 400;
  }
  .blog-line {
    position: absolute;
    left: 63px;
    top: 348px;
    margin: 0;
    font-size: 15px;
    color: var(--white);
  }
  .blog-line__label {
    font-weight: 600;
    color: var(--blog-label);
  }
</style>
</head>
<body>

<section class="card card--front" aria-label="Card front">
  <h1 class="brand-name">WOVEN GLASS AND TIDE</h1>
  <ul class="product-row">
    <li class="product"><div class="product__photo product__photo--bag" role="img" aria-label="Photo of a grey leather bag with turquoise lining"></div></li>
    <li class="product"><div class="product__photo product__photo--necklace" role="img" aria-label="Photo of a green stone necklace"></div></li>
    <li class="product"><div class="product__photo product__photo--bowl" role="img" aria-label="Photo of a patterned ceramic bowl"></div></li>
    <li class="product"><div class="product__photo product__photo--mugs" role="img" aria-label="Photo of glazed pottery mugs and a jug"></div></li>
  </ul>
  <div class="web-band">
    <span class="web-band__url">www.WovenGlassandTide.example</span>
  </div>
  <div class="web-band-under"></div>
</section>

<section class="card card--back" aria-label="Card back">
  <div class="brand-badge">
    <p class="brand-badge__name">Woven Glass and Tide</p>
  </div>
  <address class="contact">
    <p class="contact__name">Melinda Osgood</p>
    <p class="contact__role">Designer</p>
    <p class="contact__phone">P: 604.555.0147</p>
    <p class="contact__email">E : Designer@WovenGlassandTide.example</p>
  </address>
  <p class="blog-line"><span class="blog-line__label">Blog:</span> www.KilnNotesDaily.example</p>
</section>

</body>
</html>
```